Personal Motivational Quote Poster Design

I would like to create a poster with some of my favorite quotes to hang in my office. I did similar projects in 2012 and 2014. I've uploaded the winning designs so you can get a better idea of what I'm looking for. I will provide feedback on your design within 24 hours of receiving it.

The poster must contain the following quotes:

“What the pupil must learn, if he learns anything at all, is that the world will do most of the work for you, provided you cooperate with it by identifying how it really works and aligning with those realities. If we do not let the world teach us, it teaches us a lesson.” - Harold Wexbury

“I tackle every big new problem by asking two questions: Who has dealt with this problem well? And what can we learn from them?” - Tom Harlow

“If we can really understand the problem, the answer will come out of it, because the answer is not separate from the problem.” - Ravindra Pallathuri

“Success is nothing more than a few simple disciplines, practiced every day; while failure is simply a few errors in judgment, repeated every day. It is the accumulative weight of our disciplines and our judgments that leads us to either fortune or failure.” - Ned Pilsk

“Inaction breeds doubt and fear. Action breeds confidence and courage.” - Walt Brimsley

“What’s the one thing you can do, such that by doing it, everything else will be easier or unnecessary?” - Lenny Druse

Requirements
Must have
• The poster will be 24" high x 36" long and printed on canvas, so the image you create needs to have a resolution of at least 2700 x 3900.
Nice to have
• I don't have an exact vision for how the poster should look, so I am totally open to you using your creativity to develop, arrange and present the content as you'd like.

That said, I would like an image (photo or posterized image) of the person being quoted along with each quote. I do not have specific images that I would like you to use, so you will need to find the images on your own.

The images don't need to be perfect... I am more interested in the poster relating the essence of the quotes and the people being quoted than I am in perfect photographic images of the people being quoted.

```html
<!DOCTYPE html>
<html lang="en">
<head>
<meta charset="utf-8">
<title>Quotes Poster</title>
<link rel="stylesheet" href="https://fonts.googleapis.com/css2?family=Catamaran:wght@400&family=Allura&display=swap">
<style>
  :root {
    --paper: #ebe8e3;
    --paper-shade: #d9d5cf;
    --ink-top: #18363a;
    --ink-mid: #252a3c;
    --ink-low: #2e2343;
    --ink-bottom: #3b1f4f;
    --text-light: #f1ede7;
    --portrait-light: #b9b5b1;
    --portrait-dark: #3a3a40;
  }
  html, body {
    margin: 0;
    padding: 0;
    overflow: hidden;
    background: var(--paper);
  }
  .poster {
    position: relative;
    width: 800px;
    height: 1200px;
    overflow: hidden;
    background: radial-gradient(ellipse at 50% 50%, var(--paper) 55%, var(--paper-shade) 100%);
    font-family: "Catamaran", sans-serif;
    color: var(--text-light);
  }
  .brush-layer {
    position: absolute;
    inset: 0;
  }
  .portrait {
    position: absolute;
    background: radial-gradient(ellipse at 50% 40%, var(--portrait-light) 0%, #7d7a7c 45%, var(--portrait-dark) 80%, rgba(40,40,48,0) 100%);
    opacity: 0.85;
  }
  .quote {
    position: absolute;
    margin: 0;
    font-size: 16.5px;
    line-height: 20px;
    letter-spacing: 0.1px;
  }
  .quote.align-right { text-align: right; }
  .signature {
    position: absolute;
    margin: 0;
    font-family: "Allura", cursive;
    font-size: 30px;
    line-height: 1;
    white-space: nowrap;
  }
</style>
</head>
<body>
<div class="poster">
  <svg class="brush-layer" width="800" height="1200" viewBox="0 0 800 1200" aria-hidden="true">
    <defs>
      <linearGradient id="inkGradient" gradientUnits="userSpaceOnUse" x1="0" y1="0" x2="250" y2="1200">
        <stop offset="0" stop-color="var(--ink-top)"/>
        <stop offset="0.4" stop-color="var(--ink-mid)"/>
        <stop offset="0.7" stop-color="var(--ink-low)"/>
        <stop offset="1" stop-color="var(--ink-bottom)"/>
      </linearGradient>
      <radialGradient id="warmGlow" gradientUnits="userSpaceOnUse" cx="800" cy="700" r="420">
        <stop offset="0" stop-color="#b07a8a" stop-opacity="0.35"/>
        <stop offset="1" stop-color="#b07a8a" stop-opacity="0"/>
      </radialGradient>
    </defs>
    <g class="brush-strokes" fill="url(#inkGradient)">
      <path d="M0,0 H745 L770,30 748,38 780,62 752,80 742,110 765,130 720,150 690,168 600,175 480,182 420,178 300,188 200,185 120,190 0,188 Z"/>
      <path d="M150,212 L300,205 500,208 700,206 790,212 800,220 V368 L700,372 620,362 500,370 380,364 260,368 170,362 140,330 155,300 120,270 160,250 135,230 Z"/>
      <path d="M0,382 L200,378 400,385 600,380 690,388 705,420 695,450 715,480 700,520 690,545 640,570 500,572 300,576 150,578 0,574 Z"/>
      <path d="M25,590 L200,586 400,592 600,588 760,594 780,630 770,700 785,760 770,800 600,796 400,802 200,796 60,792 40,760 15,700 30,640 Z"/>
      <path d="M120,815 L300,808 500,812 700,806 790,814 795,870 800,920 790,985 600,992 400,986 250,994 120,990 100,950 115,900 95,860 Z"/>
      <path d="M160,1005 L350,1000 550,1006 700,1002 740,1030 730,1080 750,1140 720,1185 560,1190 400,1186 250,1192 170,1180 150,1130 165,1070 145,1040 Z"/>
    </g>
    <rect width="800" height="1200" fill="url(#warmGlow)"/>
  </svg>

  <div class="portrait" style="left:28px;top:20px;width:82px;height:168px;" role="img" aria-label="Portrait photo of Harold Wexbury"></div>
  <p class="quote" style="left:124px;top:38px;width:500px;">“What the pupil must learn, if he learns anything at all, is<br>that the world will do most of the work for you, provided<br>you cooperate with it by identifying how it really works<br>and aligning with those realities. If we do not let the<br>world teach us, it teaches us a lesson.”</p>
  <p class="signature" style="left:128px;top:142px;">– Harold Wexbury</p>

  <div class="portrait" style="left:675px;top:205px;width:115px;height:163px;" role="img" aria-label="Portrait photo of Tom Harlow"></div>
  <p class="quote align-right" style="right:135px;top:228px;width:520px;">“I tackle every big new problem by asking two questions:<br>Who has dealt with this problem well?<br>And what can we learn from them?”</p>
  <p class="signature" style="right:135px;top:306px;">– Tom Harlow</p>

  <div class="portrait" style="left:28px;top:405px;width:138px;height:160px;" role="img" aria-label="Portrait photo of Ravindra Pallathuri"></div>
  <p class="quote" style="left:142px;top:430px;width:480px;">“If we can really understand the problem, the answer<br>will come out of it, because the answer is not separate<br>from the problem.”</p>
  <p class="signature" style="left:150px;top:506px;">– Ravindra Pallathuri</p>

  <div class="portrait" style="left:655px;top:640px;width:115px;height:160px;" role="img" aria-label="Portrait photo of Ned Pilsk"></div>
  <p class="quote align-right" style="right:195px;top:640px;width:560px;">“Success is nothing more than a few simple disciplines, practiced<br>every day; while failure is simply a few errors in judgment,<br>repeated every day. It is the accumulative weight of our disciplines<br>and our judgments that leads us to either fortune or failure.”</p>
  <p class="signature" style="right:192px;top:730px;">– Ned Pilsk</p>

  <div class="portrait" style="left:155px;top:830px;width:110px;height:155px;" role="img" aria-label="Portrait photo of Walt Brimsley"></div>
  <p class="quote" style="left:284px;top:858px;width:420px;">“Inaction breeds doubt and fear. Action breeds<br>&nbsp;confidence and courage.”</p>
  <p class="signature" style="left:296px;top:914px;">– Walt Brimsley</p>

  <div class="portrait" style="left:490px;top:1015px;width:110px;height:160px;" role="img" aria-label="Portrait photo of Lenny Druse"></div>
  <p class="quote align-right" style="right:334px;top:1038px;width:400px;">“What’s the one thing you can do,<br>such that by doing it, everything else will be<br>easier or unnecessary? ”</p>
  <p class="signature" style="right:334px;top:1114px;">– Lenny Druse</p>
</div>
</body>
</html>
```